Dr. Lumora needs a design for its website!

*Only need the design, coding is not required.
*Need desktop version ($500) and mobile/tablet version ($200)
*The attached files are not the exact layout we want, they are just for you to know what information should be included in those pages.
*The function of our website is like www.qavlo.hk
*For the background picture, prefer a lively picture and chinese people in it, NOT necessarily need a doctor or sick person in the picture

***Don't just copy the layout from the attachments or from the reference website, we are looking for creative ideas, non-ordinary designs!!!****

We are developing a website for the public to search a doctor by different criteria. At the initial stage, we need 4 pages to start with and other pages at later stage. I have attached the general idea of these pages but not necessarily to be exactly the same, I am looking for some new ideas.

This website needs a professional, modern, simple and user friendly design. The main color to be used in the website will be same as the color (R:0 G:139 B:205) used in our logo (see attached). We don't have any particular thoughts for the other color and the font to be used in the website. Can try to use circle outline for the icon in the navigation bar.

1. Home: will include 4 sections (see attached)

2. Doctor's details (see attached)

3. Health information: will include a short descriptions of this Health Info page and 5 sections (see attached)

4. News (see attached)

Reason: Not too many suitable designs to choose from and need more time to go through the designs

All

Medical

4 page

• must not be same as or looks too much like www.qavlo.hk
• prefer not to use black and red color

```html
<!DOCTYPE html>
<html lang="en">
<head>
<meta charset="utf-8">
<title>Dr. Lumora – Home</title>
<link href="https://fonts.googleapis.com/css2?family=Carlito:wght@400;700&family=Open+Sans:wght@400;700&family=Questrial&display=swap" rel="stylesheet">
<style>
:root{
  --brand:#008bcd;
  --brand-dark:#0a7fc0;
  --ink:#3a3a3a;
  --muted:#9a9a9a;
  --line:#c9c9c9;
  --panel-line:#d6d6d6;
  --page:#f4f4f4;
  --white:#ffffff;
}
*{box-sizing:border-box;margin:0;padding:0}
html,body{width:1200px;height:1183px;overflow:hidden}
body{position:relative;background:var(--page);font-family:"Questrial",sans-serif;color:var(--ink)}
.abs{position:absolute}

/* top strip */
.topbar{left:0;top:0;width:1200px;height:20px;background:var(--brand)}
.lang{top:3px;height:14px;display:flex;align-items:center;gap:5px;font-family:"Carlito",sans-serif;font-size:9px;color:var(--white)}
.lang .dot{width:13px;height:13px;border-radius:50%;background:var(--white);opacity:.9}
.lang-en{left:992px}
.lang-zh{left:1064px}
.lang-sep{left:1055px;top:3px;width:1px;height:14px;background:#9bd3ef}

/* header */
.header{left:0;top:20px;width:1200px;height:130px;background:var(--white);box-shadow:0 2px 4px rgba(0,0,0,.08)}
.brand{left:70px;top:60px;display:flex;align-items:center;gap:12px}
.brand .mark{width:52px;height:52px;border-radius:50%;background:var(--brand)}
.brand .name{font-family:"Questrial",sans-serif;font-size:40px;color:var(--brand)}
.search{left:726px;top:45px;width:268px;height:32px;border:1px solid #d4d4d4;border-radius:16px;background:var(--white)}
.search span{position:absolute;left:15px;top:7px;font-size:14px;color:#c2c2c2}
.search svg{position:absolute;right:11px;top:6px}
.login{left:1031px;top:45px;width:90px;height:32px;background:var(--brand);color:var(--white);font-size:15px;display:flex;align-items:center;justify-content:center}
.nav{top:103px;font-size:14.5px;color:var(--brand)}

/* hero */
.hero{left:0;top:150px;width:1200px;height:580px;
  background:linear-gradient(90deg,#b9a699 0%,#d8c9bf 25%,#cbb8aa 45%,#e6ddd5 60%,#f4f1ee 75%,#f7f6f4 100%)}
.hero-title{left:540px;top:219px;width:620px;text-align:right;white-space:nowrap;font-family:"Open Sans",sans-serif;font-weight:700;font-size:38px;line-height:48px;color:var(--brand);letter-spacing:-.4px}
.perk{left:704px;font-size:26.5px;color:var(--ink);display:flex;align-items:center;height:34px;white-space:nowrap}
.perk svg{margin-right:19px}
.signup{left:830px;top:610px;width:138px;height:51px;background:var(--brand);color:var(--white);font-size:21px;display:flex;align-items:center;justify-content:center}

/* panels */
.panel{top:758px;height:380px;background:var(--white);border:1px solid var(--panel-line);border-radius:12px}
.panel-find{left:30px;width:522px}
.panel-results{left:568px;width:600px}
.find-icon{left:62px;top:781px;width:22px;height:22px;border-radius:50%;border:2px solid var(--brand)}
.find-title{left:108px;top:777px;font-family:"Carlito",sans-serif;font-size:28px;color:var(--brand)}
.label{font-family:"Carlito",sans-serif;font-size:14px;color:var(--ink)}
.field{background:var(--white);border:1px solid var(--line);border-radius:4px}
.select{background:var(--white);border:1px solid var(--line);font-family:"Carlito",sans-serif;font-size:10px;color:#b0b0b0;padding:3px 8px}
.select i{position:absolute;right:0;top:0;width:19px;height:100%;border-left:1px solid var(--line)}
.select i:after{content:"";position:absolute;left:5px;top:6px;border:4px solid transparent;border-top:5px solid #444}
.radio{width:13px;height:13px;border-radius:50%;border:1px solid #888;background:var(--white)}
.radio.on:after{content:"";position:absolute;left:2px;top:2px;width:7px;height:7px;border-radius:50%;background:#333}
.opt{font-family:"Carlito",sans-serif;font-size:12px;color:var(--ink)}
.btn{top:1084px;width:84px;height:26px;font-size:13px;display:flex;align-items:center;justify-content:center}
.btn-reset{left:191px;border:1px solid var(--brand);color:var(--brand);background:var(--white)}
.btn-search{left:308px;background:var(--brand);color:var(--white)}
.empty{left:782px;top:934px;display:flex;align-items:center;gap:10px;font-family:"Carlito",sans-serif;font-size:17px;color:var(--brand)}
.footer{left:0;top:1157px;width:1200px;text-align:center;font-family:"Carlito",sans-serif;font-size:10px;color:#777}
</style>
</head>
<body>

<div class="abs topbar"></div>
<div class="abs lang lang-en"><span class="dot"></span>ENGLISH</div>
<div class="abs lang-sep"></div>
<div class="abs lang lang-zh"><span class="dot"></span>CHINESE</div>

<header class="abs header"></header>
<div class="abs brand"><span class="mark"></span><span class="name">Dr. Lumora</span></div>
<div class="abs search"><span>Search . . .</span>
  <svg width="20" height="20" viewBox="0 0 20 20" fill="none" stroke="#008bcd" stroke-width="1.5"><circle cx="8" cy="8" r="6.5"/><line x1="12.8" y1="12.8" x2="18" y2="18"/></svg>
</div>
<div class="abs login">LOG IN</div>
<nav>
  <span class="abs nav" style="left:462px">Home</span>
  <span class="abs nav" style="left:554px">Doctor List</span>
  <span class="abs nav" style="left:677px">Health Information</span>
  <span class="abs nav" style="left:847px">News</span>
  <span class="abs nav" style="left:938px">About Us</span>
  <span class="abs nav" style="left:1052px">Contact Us</span>
</nav>

<section class="abs hero" role="img" aria-label="Photo of three young women laughing together over coffee cups at a bright table"></section>
<h1 class="abs hero-title">Become a Dr. Lumora Member</h1>
<div class="abs perk" style="top:296px"><svg width="22" height="26" viewBox="0 0 22 26"><path d="M2 15 L8 23 L20 2" fill="none" stroke="#008bcd" stroke-width="3"/></svg>First- hand health news</div>
<div class="abs perk" style="top:356px"><svg width="22" height="26" viewBox="0 0 22 26"><path d="M2 15 L8 23 L20 2" fill="none" stroke="#008bcd" stroke-width="3"/></svg>Exclusive promotions</div>
<div class="abs perk" style="top:416px"><svg width="22" height="26" viewBox="0 0 22 26"><path d="M2 15 L8 23 L20 2" fill="none" stroke="#008bcd" stroke-width="3"/></svg>Instant health advices</div>
<div class="abs perk" style="top:476px"><svg width="22" height="26" viewBox="0 0 22 26"><path d="M2 15 L8 23 L20 2" fill="none" stroke="#008bcd" stroke-width="3"/></svg>Free health seminars or talk</div>
<div class="abs perk" style="top:536px"><svg width="22" height="26" viewBox="0 0 22 26"><path d="M2 15 L8 23 L20 2" fill="none" stroke="#008bcd" stroke-width="3"/></svg>Priority doctor appointments</div>
<div class="abs signup">SIGN UP</div>

<section class="abs panel panel-find"></section>
<div class="abs find-icon"></div>
<h2 class="abs find-title" style="font-weight:400">Find a Doctor</h2>

<span class="abs label" style="left:55px;top:841px">Doctor’s Name:</span>
<div class="abs field" style="left:157px;top:839px;width:369px;height:24px"></div>

<span class="abs label" style="left:55px;top:893px">Gender:</span>
<div class="abs radio on" style="left:120px;top:896px"></div>
<span class="abs opt" style="left:141px;top:895px">Male</span>
<div class="abs radio" style="left:182px;top:896px"></div>
<span class="abs opt" style="left:204px;top:895px">Female</span>
<span class="abs label" style="left:276px;top:893px">Phone Number:</span>
<div class="abs field" style="left:380px;top:894px;width:146px;height:17px;border-radius:2px"></div>

<span class="abs label" style="left:55px;top:937px">Specialism:</span>
<div class="abs select" style="left:138px;top:938px;width:170px;height:17px">Select a specialism<i></i></div>
<span class="abs label" style="left:55px;top:984px">Symptoms:</span>
<div class="abs select" style="left:138px;top:985px;width:170px;height:17px">Select a symptom<i></i></div>
<span class="abs label" style="left:55px;top:1033px">District:</span>
<div class="abs select" style="left:138px;top:1034px;width:170px;height:17px">Select a district<i></i></div>

<div class="abs btn btn-reset">RESET</div>
<div class="abs btn btn-search">SEARCH</div>

<section class="abs panel panel-results"></section>
<div class="abs empty">
  <svg width="20" height="22" viewBox="0 0 20 22" fill="none" stroke="#008bcd" stroke-width="1.6"><circle cx="8" cy="8" r="6.5"/><line x1="12.5" y1="13" x2="18" y2="20"/></svg>
  No Results Found
</div>

<footer class="abs footer">© Dr. Lumora. All Rights Reserved.</footer>
</body>
</html>
```